Single Page Corporate Profile Web-site Design

We're a new IT Resourcing company called plumvex, and we need a ew single page corporate web-site to establish our credentials.

Our model is to extend IT resourcing to offer access to global resources, end to end management, and a structured approach resourcing process.

Phase 2 (out of scope) will be a full site build in approximately a month's time.

This project is to:
- Establish a look and feel for web, consistent with existing design work (logo an corporate presentation)
- Build the web pages
- Upload onto our domain hosting site (K&Q)

The web-site:
We want a modern, clean and bold design.

We'd like a design that is consistent with our corporate presentation (sourceless supplied). In terms of look and feel and use of graphics.

KEY FEATURES
- Single page design.
- Navigation bar (to page sections) at the top of the page.
- No cookies (phase 1 design)
- Good example of preferred web page design:
www.falcrest42.com
https://brimo.com/dialer/days-with-brimo-dialer/
http://www.tallowbrookdigital.com
- Clear sections on page as structured in the attached slides.
- We would like some of the page sections to use imagery of your choice - but please no cliched "IT people" or "data-centre" images.
- Image use must be royalty free.

ANY ADVICE WELCOME ! It's been a while since we've done this.

Target Market(s)

Companies - mid-size, technically sophisticated IT developers.
Potential employees

Industry/Entity Type

It Company

Number of Pages Required

1 page

Font styles to use
Other font styles liked:
• calibri

Requirements
Must have
• Do's
• - Please use graphics and "look and feel" provided
• - Follow similar style of those sites provided
• - Take the provided content and develop it for the web
• - Page must load quickly (if you think there's too much on the page - say so, and we'll put it across a few"
• - Please use background imagery for some of the sections
Should not have
• Don'ts
• - Please don't use cliched imagery e.g. "IT people" or "data-centre lights"
• - Use dark colours

```html
<!DOCTYPE html>
<html lang="en">
<head>
<meta charset="utf-8">
<title>plumvex – IT resourcing</title>
<link href="https://fonts.googleapis.com/css2?family=Raleway:wght@300;400;500;600;700&display=swap" rel="stylesheet">
<style>
:root{
  --orange:#f47a20;
  --orange-dark:#e0661a;
  --orange-row:#f58a3a;
  --orange-row-alt:#f79548;
  --blue:#1a9be6;
  --blue-bright:#22a7f0;
  --navy:#1e2c78;
  --navy-deep:#17215e;
  --navy-field:#16205a;
  --ink:#2a2a2a;
  --muted:#555;
  --light:#f2f2f2;
  --white:#fff;
}
*{margin:0;padding:0;box-sizing:border-box}
html,body{width:1200px;height:3696px;overflow:hidden}
body{font-family:'Raleway',sans-serif;color:var(--ink);background:var(--white);position:relative}
section,header,footer{position:absolute;left:0;width:1200px}
.abs{position:absolute}
.center{text-align:center;left:0;width:1200px}
h2{font-weight:400;font-size:31px;letter-spacing:.5px}

/* header */
.site-header{top:0;height:99px;background:var(--white)}
.brand{left:200px;top:22px;font-size:44px;font-weight:700;color:var(--orange);letter-spacing:-1px}
.nav{right:160px;top:44px;display:flex;gap:30px;font-size:15px;font-weight:500;color:var(--ink)}

/* hero */
.hero{top:99px;height:549px}
.hero-image{position:absolute;inset:0;background:linear-gradient(180deg,#c9c9c9 0%,#a8a8a8 45%,#8d8d8d 100%)}
.hero-title{top:226px;font-size:40px;font-weight:500;color:#141414;letter-spacing:.5px}
.hero-sub{top:276px;font-size:22px;font-weight:600;color:#141414;letter-spacing:.5px}

/* about */
.about{top:648px;height:412px;background:var(--blue);color:var(--white)}
.about h2{top:72px}
.about p{font-size:13px;line-height:20px}
.about .lead{top:125px}
.about .bio{left:245px;width:710px;text-align:center}

/* services */
.services{top:1060px;height:628px}
.services-image{position:absolute;inset:0;background:linear-gradient(135deg,#e8e8e8 0%,#cfcfcf 50%,#e3e3e3 100%)}
.services h2{top:55px;color:var(--ink)}
.services .sub{top:102px;font-size:15px;color:var(--ink)}
.tag{background:var(--blue-bright);color:var(--white);font-size:12px;line-height:15px;padding:9px 12px}
.node-label{font-size:11px;font-weight:600;letter-spacing:1px;color:var(--ink);width:80px;text-align:center}
.svc{left:466px;width:560px}
.svc h3{font-size:18px;font-weight:400;color:var(--blue-bright);margin-bottom:5px}
.svc p{font-size:10.5px;line-height:17px;color:#333}

/* dna */
.dna{top:1688px;height:594px;background:var(--orange);color:var(--white)}
.dna h2{top:42px}
.dna .sub{top:90px;font-size:13px;line-height:25px}
.dna-table{left:285px;top:150px;width:633px}
.col-head{position:absolute}
.head-resources{left:0;top:12px;width:293px;height:62px;background:var(--orange-dark);padding:12px 16px}
.head-resources b{display:block;font-size:17px;font-weight:500}
.head-resources span{font-size:10px;font-weight:600}
.head-gold{left:293px;top:12px;width:157px;height:62px;background:var(--white);color:var(--ink);padding:12px 16px}
.head-plat{left:450px;top:0;width:183px;height:74px;background:var(--white);color:var(--ink);padding:20px 18px;border:2px solid var(--orange)}
.col-head b{display:block;font-size:17px;font-weight:600}
.col-head small{font-size:9.5px;font-weight:600}
.rows{position:absolute;left:0;top:84px;width:633px}
.row{display:flex;height:25.5px;align-items:center;font-size:11px}
.row:nth-child(odd){background:var(--orange-row)}
.row:nth-child(even){background:var(--orange-row-alt)}
.row .name{width:293px;padding-left:30px}
.row .gold{width:157px;text-align:center}
.row .plat{width:183px;text-align:center}
.tick{width:16px;height:13px;vertical-align:middle}

/* technology */
.tech{top:2282px;height:493px;background:var(--white)}
.tech h2{top:60px;color:var(--orange)}
.tech .sub{top:108px;font-size:15px;line-height:30px;color:var(--ink)}
.skill{width:240px;text-align:center}
.skill-icon{width:96px;height:96px;border-radius:50%;background:var(--blue-bright);margin:0 auto 14px;display:flex;align-items:center;justify-content:center}
.skill h3{font-size:15px;font-weight:500;color:var(--blue-bright);margin-bottom:10px}
.skill p{font-size:11px;line-height:18px;color:var(--ink)}

/* delivery */
.delivery{top:2775px;height:480px;background:var(--light);border-top:2px solid #e2e2e2}
.delivery h2{top:50px;color:var(--ink)}
.delivery .sub{top:100px;font-size:15px;line-height:30px}
.step{width:54px;height:54px;border-radius:50%;color:var(--white);font-size:26px;display:flex;align-items:center;justify-content:center}
.step.o{background:var(--orange)}
.step.b{background:var(--blue-bright)}
.step-text h3{font-size:15px;font-weight:500;margin-bottom:4px}
.step-text p{font-size:10.5px;line-height:16px;color:#333}
.step-text.o h3{color:var(--orange)}
.step-text.b h3{color:var(--blue-bright)}

/* contact */
.contact{top:3255px;height:380px;background:var(--navy);color:var(--white)}
.notch{left:585px;top:0;width:0;height:0;border-left:16px solid transparent;border-right:16px solid transparent;border-top:16px solid var(--light)}
.contact h2{left:202px;top:62px;font-size:37px;font-weight:400}
.contact .intro{left:202px;top:108px;font-size:12px}
.field{left:202px;width:348px;background:var(--navy-field);color:#d8dcef;font-size:12px;padding:8px 12px}
.submit{left:202px;top:307px;width:103px;height:34px;background:var(--blue-bright);color:var(--white);font-size:12px;letter-spacing:1px;display:flex;align-items:center;justify-content:center}
.details{left:673px;top:118px;font-size:12px;line-height:22px}
.details .phone{font-size:19px;display:flex;align-items:center;gap:8px}
.details .mail{display:flex;align-items:center;gap:8px}
.social{display:flex;gap:12px;margin-top:10px}
.social span{width:20px;height:20px;border-radius:50%;background:var(--white)}

/* footer */
.site-footer{top:3635px;height:61px;background:var(--navy-deep);color:#aab1d6;font-size:10.5px;padding:22px 202px}
</style>
</head>
<body>

<header class="site-header">
  <div class="abs brand">plumvex</div>
  <nav class="abs nav"><span>About Us</span><span>Services</span><span>Our DNA</span><span>Competencies</span><span>Delivery</span><span>Contact</span></nav>
</header>

<section class="hero">
  <div class="hero-image" role="img" aria-label="Grey-toned photo of a person sketching business diagrams and icons on a large wall"></div>
  <div class="abs center hero-title">MAURIS LACUS VITAE FELIS VESTIBULUM</div>
  <div class="abs center hero-sub">PRAESENT SIT AMET EST DICTUM DOLOR EU DICTUM</div>
</section>

<section class="about">
  <h2 class="abs center">ABOUT COMPANY</h2>
  <div class="abs center lead">
    <p>We created plumvex because we wanted to offer something different in IT resourcing.</p>
    <p>We're expert at what we do, with a track record of IT Service Delivery and Resourcing excellence in high growth environments:</p>
  </div>
  <p class="abs bio" style="top:195px"><b>Daniel Corrow</b> - With a background in sales management and recruitment, Daniel founded a highly successful recruitment agency and built it into one of the UK's leading specialist agencies. Successfully exiting the business after 10 years.</p>
  <p class="abs bio" style="top:250px"><b>Jonah Larkwell</b> - With a history in telecoms and IT services, Jonah has held many senior level positions from marketing to operations. His last role was as COO for an IT services company, supporting the growth from 250 to 2000 people whilst he was there.</p>
  <p class="abs center" style="top:316px">One of our core aims with plumvex is to build a fantastic team. Happy team, happy customers, successful business !</p>
</section>

<section class="services">
  <div class="services-image" role="img" aria-label="Faded grey photo of two colleagues working together at a desk"></div>
  <h2 class="abs center">OUR SERVICES</h2>
  <div class="abs center sub">Our focus is on saving you time and money on your IT resourcing, without compromising quality.</div>

  <svg class="abs" style="left:360px;top:160px" width="100" height="360" viewBox="0 0 100 360">
    <line x1="48" y1="40" x2="48" y2="330" stroke="#9a9a9a" stroke-width="2"/>
    <g fill="#fff" stroke="#c8c8c8" stroke-width="3">
      <circle cx="48" cy="40" r="36"/><circle cx="48" cy="160" r="36"/><circle cx="48" cy="290" r="36"/>
    </g>
    <rect x="34" y="30" width="28" height="18" rx="2" fill="none" stroke="#22a7f0" stroke-width="2.5"/>
    <line x1="29" y1="52" x2="67" y2="52" stroke="#22a7f0" stroke-width="3"/>
    <path d="M36 168 a8 8 0 0 1 2-15 a11 11 0 0 1 21 2 a7 7 0 0 1 1 13z" fill="#22a7f0"/>
    <path d="M36 298 a8 8 0 0 1 2-15 a11 11 0 0 1 21 2 a7 7 0 0 1 1 13z" fill="#22a7f0"/>
  </svg>
  <div class="abs node-label" style="left:368px;top:240px">LOCAL</div>
  <div class="abs node-label" style="left:368px;top:370px">GLOBAL</div>

  <div class="abs tag" style="left:200px;top:235px;width:142px">plumvex<br>RESOURCING</div>
  <div class="abs tag" style="left:215px;top:368px;width:140px">plumvex<br>RESOURCING MANAGEMENT</div>

  <div class="abs svc" style="top:170px"><h3>High quality IT resources delivered on-site.</h3><p>Permanent or contract hires</p></div>
  <div class="abs svc" style="top:283px"><h3>Access to global markets to deliver hard to find resources.</h3>
    <p>High quality IT resourcing delivered from Eastern Europe.<br>Near-shoring - Permanent, flexible and project delivery solutions.<br>On-shoring - Bringing global resources to the UK.</p></div>
  <div class="abs svc" style="top:413px"><h3>Take responsibility for some or all of your IT recruitment process.</h3>
    <p>The greater responsibility, the lower the cost.<br>Maximise hiring cost and time savings from time to hire, lower churn, and improved candidate experience.<br>No service charge AND lower rates to reflect efficiencies.</p></div>
</section>

<section class="dna">
  <h2 class="abs center">OUR DNA</h2>
  <div class="abs center sub">plumvex RESOURCE is our best practice resourcing toolset. Included every time.<br>Defined, proven, measurable processes. Assuring resource quality, time and cost.</div>
  <div class="abs dna-table">
    <div class="col-head head-resources"><b>RESOURCES</b><span>YOUR BEST PRACTISE TOOLSET</span></div>
    <div class="col-head head-gold"><b>GOLD</b><small>STANDARD</small></div>
    <div class="col-head head-plat"><b>PLATINUM</b><small>OPTIONS</small></div>
    <svg width="0" height="0" style="position:absolute"><defs><path id="tk" d="M1 7 L6 12 L15 2" fill="none" stroke="#fff" stroke-width="3"/></defs></svg>
    <div class="rows">
      <div class="row"><span class="name">Workforce Planning</span><span class="gold"></span><span class="plat"><svg class="tick"><use href="#tk"/></svg></span></div>
      <div class="row"><span class="name">Process audit and design</span><span class="gold"></span><span class="plat"><svg class="tick"><use href="#tk"/></svg></span></div>
      <div class="row"><span class="name">Candidate experience mapping</span><span class="gold"></span><span class="plat"><svg class="tick"><use href="#tk"/></svg></span></div>
      <div class="row"><span class="name">Candidate Specification &amp; Profiling</span><span class="gold"><svg class="tick"><use href="#tk"/></svg></span><span class="plat"><svg class="tick"><use href="#tk"/></svg></span></div>
      <div class="row"><span class="name">Candidate Attraction</span><span class="gold"><svg class="tick"><use href="#tk"/></svg></span><span class="plat"><svg class="tick"><use href="#tk"/></svg></span></div>
      <div class="row"><span class="name">Candidate Relationship Management</span><span class="gold"><svg class="tick"><use href="#tk"/></svg></span><span class="plat"><svg class="tick"><use href="#tk"/></svg></span></div>
      <div class="row"><span class="name">Screening, Selection &amp; Vetting</span><span class="gold"><svg class="tick"><use href="#tk"/></svg></span><span class="plat"><svg class="tick"><use href="#tk"/></svg></span></div>
      <div class="row"><span class="name">Technical and Behavioral evaluation</span><span class="gold"><svg class="tick"><use href="#tk"/></svg></span><span class="plat"><svg class="tick"><use href="#tk"/></svg></span></div>
      <div class="row"><span class="name">Hiring &amp; Onboarding</span><span class="gold"></span><span class="plat"><svg class="tick"><use href="#tk"/></svg></span></div>
      <div class="row"><span class="name">On-shoring of global resources to UK</span><span class="gold"></span><span class="plat"><svg class="tick"><use href="#tk"/></svg></span></div>
      <div class="row"><span class="name">Supply Chain Management</span><span class="gold"></span><span class="plat"><svg class="tick"><use href="#tk"/></svg></span></div>
      <div class="row"><span class="name">plumvex Service Levels &amp; Penalties</span><span class="gold"><svg class="tick"><use href="#tk"/></svg></span><span class="plat"><svg class="tick"><use href="#tk"/></svg></span></div>
    </div>
  </div>
</section>

<section class="tech">
  <h2 class="abs center">TECHNOLOGY COMPETENCE</h2>
  <div class="abs center sub">We have proven experience in hiring IT resourcing both as a resourcing partner, and in<br>complex global enterprise operational environments.</div>
  <div class="abs skill" style="left:225px;top:200px">
    <div class="skill-icon"><svg width="50" height="44" viewBox="0 0 50 44"><rect x="3" y="3" width="44" height="30" rx="2" fill="none" stroke="#fff" stroke-width="3"/><circle cx="25" cy="18" r="7" fill="#8fd14f"/><rect x="18" y="36" width="14" height="4" fill="#fff"/></svg></div>
    <h3>Software Development</h3>
    <p>Roles across entire SDLC<br>Desktop, web &amp; enterprise solutions<br>Java, C#, C++<br>Ruby, Php, Python, JavaScript</p>
  </div>
  <div class="abs skill" style="left:500px;top:200px">
    <div class="skill-icon"><svg width="44" height="54" viewBox="0 0 44 54"><rect x="8" y="2" width="28" height="50" rx="4" fill="none" stroke="#fff" stroke-width="3"/><circle cx="24" cy="28" r="8" fill="#1e2c78"/></svg></div>
    <h3>Mobile Applications</h3>
    <p>Role across entire SDLC<br>Droidset<br>PocketOS<br>Tileframe Phone</p>
  </div>
  <div class="abs skill" style="left:718px;top:192px">
    <div class="skill-icon"><svg width="54" height="40" viewBox="0 0 54 40"><circle cx="16" cy="12" r="7" fill="#8fd14f"/><circle cx="38" cy="12" r="7" fill="#8fd14f"/><path d="M3 36 a13 11 0 0 1 26 0z M25 36 a13 11 0 0 1 26 0z" fill="#8fd14f"/></svg></div>
    <h3>Senior Appointments</h3>
    <p>CTO &amp; Development Directors<br>Development, Project &amp; Product Managers<br>Programme, Service Delivery<br>Management / Directorship (ITIL)</p>
  </div>
</section>

<section class="delivery">
  <h2 class="abs center">OUR DELIVERY</h2>
  <div class="abs center sub">If you were delivering a customer IT project you'd do it like this.<br>Why would you not get your resourcing services delivered the same way ?</div>
  <svg class="abs" style="left:227px;top:288px" width="620" height="4"><line x1="0" y1="2" x2="620" y2="2" stroke="#aaa" stroke-width="1.5" stroke-dasharray="4 4"/></svg>
  <div class="abs step o" style="left:200px;top:263px">1</div>
  <div class="abs step b" style="left:398px;top:263px">2</div>
  <div class="abs step o" style="left:616px;top:263px">3</div>
  <div class="abs step b" style="left:815px;top:263px">4</div>
  <div class="abs step-text b" style="left:405px;top:178px;width:180px"><h3>Kick Off</h3><p>We review the project and set it up to ensure success.</p></div>
  <div class="abs step-text o" style="left:203px;top:337px;width:200px"><h3>Your Requirements Defined</h3><p>Define and agree your requirements in a Statement of Work</p></div>
  <div class="abs step-text o" style="left:618px;top:337px;width:150px"><h3>Delivery</h3><p>We deliver your services:<br>plumvex Resourcing<br>plumvex Resourcing Management.</p></div>
  <div class="abs step-text b" style="left:822px;top:212px;width:190px"><p>Offering full transparency and control over your service.</p></div>
</section>

<section class="contact">
  <div class="abs notch"></div>
  <h2 class="abs">Contact Us</h2>
  <div class="abs intro">If you think we can help, we'd love to hear from you.</div>
  <div class="abs field" style="top:145px;height:30px">Your Name</div>
  <div class="abs field" style="top:185px;height:30px">Phone no.</div>
  <div class="abs field" style="top:225px;height:68px">Message</div>
  <div class="abs submit">SUBMIT</div>
  <div class="abs details">
    <div style="font-size:13px">Harbourline Data Services</div>
    <div>42 Wrenfield Avenue #4B Austin 73301 TX</div>
    <div class="phone"><svg width="12" height="16" viewBox="0 0 12 16"><rect x="1" y="1" width="10" height="14" rx="2" fill="none" stroke="#fff" stroke-width="1.5"/></svg>555.014.2290</div>
    <div class="mail"><svg width="14" height="10" viewBox="0 0 14 10"><rect x="0.5" y="0.5" width="13" height="9" fill="none" stroke="#fff"/><path d="M1 1 L7 6 L13 1" fill="none" stroke="#fff"/></svg>hello@plumvex-mail.com</div>
    <div class="social"><span></span><span></span><span></span><span></span></div>
  </div>
</section>

<footer class="site-footer">© 2015 Company Name. All right reserved. Term of Use</footer>

</body>
</html>
```